Letterhead and Stationary for Construction Company

Lumen Forge needs modern Letterhead, Envelopes and Notepad designs.

Industry/Entity Type

Construction

Colors
f78f20
34a7d8
ffffff

Requirements
Must have
• Modern looking design.

```html
<!DOCTYPE html>
<html lang="en">
<head>
<meta charset="utf-8">
<title>Lumen Forge Letterhead</title>
<link href="https://fonts.googleapis.com/css2?family=Fira+Sans:wght@300;400;600&display=swap" rel="stylesheet">
<style>
  :root {
    --orange: #f07a27;
    --blue: #1177c0;
    --ink: #3a3a3a;
    --body: #555555;
    --paper: #ffffff;
  }
  * { margin: 0; padding: 0; box-sizing: border-box; }
  html, body { width: 848px; height: 1200px; overflow: hidden; background: var(--paper); }
  .letterhead {
    position: relative; width: 848px; height: 1200px; overflow: hidden;
    font-family: "Fira Sans", sans-serif; color: var(--body); background: var(--paper);
  }
  .side-band { position: absolute; left: 0; top: 0; }
  .brand {
    position: absolute; left: 138px; top: 130px;
    display: flex; align-items: center; gap: 10px;
  }
  .brand-dot { width: 22px; height: 22px; border-radius: 50%; background: var(--orange); }
  .brand-name { font-size: 31px; font-weight: 600; color: var(--blue); letter-spacing: -0.5px; }
  .recipient { position: absolute; left: 148px; top: 304px; font-size: 17px; color: var(--ink); font-weight: 300; }
  .recipient strong { color: var(--blue); font-weight: 600; }
  .date { position: absolute; left: 672px; top: 306px; font-size: 12.5px; font-weight: 300; color: var(--ink); }
  .body-copy {
    position: absolute; left: 140px; top: 438px; width: 619px;
    font-size: 15px; line-height: 24px; font-weight: 300; text-align: justify;
  }
  .body-copy p + p { margin-top: 24px; }
  .contact { position: absolute; font-size: 12px; font-weight: 300; color: var(--ink); line-height: 19px; }
  .contact.phone { left: 107px; top: 916px; }
  .contact.address { left: 99px; top: 971px; }
  .contact.postbox { left: 99px; top: 1048px; }
  .sign-off { position: absolute; right: 110px; top: 912px; text-align: right; color: var(--ink); }
  .sign-off .name { font-size: 16.5px; font-weight: 600; }
  .sign-off .role { font-size: 11px; font-weight: 600; margin-top: 2px; }
  .signature {
    position: absolute; left: 628px; top: 955px; width: 116px; height: 52px;
    background: linear-gradient(90deg, #f1f1f1, #e6e6e6); border-radius: 4px;
  }
  .edge-dots { position: absolute; left: 826px; top: 0; }
</style>
</head>
<body>
<div class="letterhead">
  <svg class="side-band" width="120" height="1200" viewBox="0 0 120 1200">
    <path d="M27 0 H106 V232 A40 40 0 0 0 27 232 Z" fill="var(--orange)"/>
    <circle cx="68" cy="292" r="34" fill="var(--orange)"/>
    <rect x="46" y="344" width="40" height="856" fill="var(--blue)"/>
    <g class="contact-icons">
      <circle cx="68" cy="924" r="26" fill="var(--paper)"/>
      <circle cx="68" cy="924" r="19" fill="var(--orange)"/>
      <path d="M61 917 q1 -2 3 -1 l2 4 q0 2 -2 2 q1 4 5 6 q0 -2 2 -2 l4 2 q1 2 -1 3 q-10 1 -13 -14z" fill="none" stroke="#fff" stroke-width="1.4"/>
      <circle cx="68" cy="990" r="26" fill="var(--paper)"/>
      <circle cx="68" cy="990" r="19" fill="var(--orange)"/>
      <path d="M68 1000 c-5 -6 -7 -9 -7 -12 a7 7 0 0 1 14 0 c0 3 -2 6 -7 12z" fill="none" stroke="#fff" stroke-width="1.4"/>
      <circle cx="68" cy="987" r="2.3" fill="none" stroke="#fff" stroke-width="1.3"/>
      <circle cx="68" cy="1058" r="26" fill="var(--paper)"/>
      <circle cx="68" cy="1058" r="19" fill="var(--orange)"/>
      <path d="M58 1058 L68 1049 L78 1058 M61 1056 V1066 H75 V1056 M66 1066 V1060 H70 V1066" fill="none" stroke="#fff" stroke-width="1.4"/>
    </g>
  </svg>

  <div class="brand">
    <span class="brand-dot"></span>
    <span class="brand-name">Lumen Forge</span>
  </div>

  <div class="recipient">To <strong>John Doe</strong></div>
  <div class="date">july 15 - 2018</div>

  <div class="body-copy">
    <p>Contrary to popular belief, Lorem Ipsum is not simply random text. It has roots in a piece of classical Latin literature from 45 BC, making it over 2000 years old. Daniel Whitcombe, a Latin professor at Ashbury Hill College in Virginia, looked up one of the more obscure Latin words, consectetur, from a Lorem Ipsum passage, and going through the cites of the word in classical literature, discovered the undoubtable source. Lorem Ipsum comes from sections 1.10.32 and 1.10.33 of "de Finibus Bonorum et Malorum" (The Extremes of Good and Evil) by Cicero, written in 45 BC. This book is a treatise on the theory of ethics, very popular during the Renaissance. The first line of Lorem Ipsum, "Lorem ipsum dolor sit amet..", comes from a line in section 1.10.32.</p>
    <p>The standard chunk of Lorem Ipsum used since the 1500s is reproduced below for those interested. Sections 1.10.32 and 1.10.33 from "de Finibus Bonorum et Malorum" by Cicero are also reproduced in their exact original form, accompanied by English versions from the 1914 translation by H. Ellworth.</p>
  </div>

  <div class="contact phone">00 321 55 18 42 60</div>
  <div class="contact address">Riverside - Street 4 18<br>Building 7</div>
  <div class="contact postbox">P.O.Box 5870 Postal code 30417</div>

  <div class="sign-off">
    <div class="name">Micheal Doe</div>
    <div class="role">Director</div>
  </div>
  <div class="signature" role="img" aria-label="Handwritten signature of the director"></div>

  <svg class="edge-dots" width="22" height="1200" viewBox="0 0 22 1200">
    <circle cx="22" cy="941" r="22" fill="var(--orange)"/>
    <circle cx="22" cy="1002" r="22" fill="var(--orange)"/>
    <circle cx="22" cy="1065" r="22" fill="var(--orange)"/>
  </svg>
</div>
</body>
</html>
```